10 steps to structured content!

We need a graphic that visualizes the 10 steps (see pdf vrelkit-en) to get to structured data that is suitable for cross media (omnichannel) publishing.

Prefer vector (ai, svg) and very clean + light design. No glossy effects or thick shadows needed.

Default colors are attached, but use of additional colors is no problem.

Target Market(s)

technical communication
marketing communication
product information

Industry/Entity Type

Digital Marketing

Font styles to use
Sans Serif

Colors

Designer to choose colors to be used in the design.

Requirements
Must have
• include the 10 steps from the pdf
• * either as a single graphic
• * or split into up to. 3 'slides'
Nice to have
• refer to quillforge site: https://www.quillforge.example/ovra/
• Screen: https://snapview.example/Tg8WpzLm2cQx4NaH/www.quillforge.example
• the huge blue/purple/red graphic is really modern style
Should not have
• glossy, thick borders, rich ornaments

```html
<!DOCTYPE html>
<html lang="de">
<head>
<meta charset="utf-8">
<title>Strukturierte Inhalte – Schritte</title>
<link href="https://fonts.googleapis.com/css2?family=Montserrat:wght@600;700&display=swap" rel="stylesheet">
<style>
  :root {
    --navy: #234a82;
    --teal: #27ada0;
    --orange: #f05a2a;
    --grey: #6d6e70;
    --dot: #c4c4c4;
    --bg: #ffffff;
  }
  html, body { margin: 0; padding: 0; overflow: hidden; background: var(--bg); }
  .canvas { position: relative; width: 1200px; height: 476px; overflow: hidden; background: var(--bg); }
  .step-arrow { position: absolute; }
  .step-arrow svg { display: block; }
  .step-label {
    position: absolute;
    font-family: "Montserrat", sans-serif; font-weight: 700;
    font-size: 19px; line-height: 23px; color: #fff; white-space: nowrap; letter-spacing: 0.2px;
  }
  .arrow-group { left: 54px; top: 111px; }
  .arrow-group .step-label { top: 19px; left: 13px; }
  .arrow-features { left: 483px; top: 111px; }
  .arrow-features .step-label { top: 25px; left: 6px; }
  .arrow-hierarchy { left: 875px; top: 113px; }
  .arrow-hierarchy .step-label { top: 21px; left: 15px; }
  .illustration { position: absolute; left: 0; top: 0; }
</style>
</head>
<body>
<div class="canvas">

  <div class="step-arrow arrow-group">
    <svg width="245" height="64" viewBox="0 0 245 64"><polygon fill="var(--navy)" points="0,12 208,12 208,0 245,32 208,64 208,52 0,52"/></svg>
    <span class="step-label">Inhalte gruppieren</span>
  </div>

  <div class="step-arrow arrow-features">
    <svg width="244" height="64" viewBox="0 0 244 64"><polygon fill="var(--navy)" points="0,12 207,12 207,0 244,32 207,64 207,52 0,52"/></svg>
    <span class="step-label">Merkmale definieren</span>
  </div>

  <div class="step-arrow arrow-hierarchy">
    <svg width="241" height="64" viewBox="0 0 241 64"><polygon fill="var(--navy)" points="0,12 206,12 206,0 241,32 206,64 206,52 0,52"/></svg>
    <span class="step-label">Hierarchien bilden</span>
  </div>

  <svg class="illustration" width="1200" height="476" viewBox="0 0 1200 476">
    <g class="shape-grid">
      <rect x="59" y="207" width="22" height="22" fill="var(--teal)"/>
      <polygon points="120,207 132,227 108,227" fill="var(--orange)"/>
      <circle cx="169" cy="218" r="12" fill="var(--navy)"/>
      <circle cx="219" cy="218" r="12" fill="var(--navy)"/>

      <circle cx="70" cy="263" r="12" fill="var(--navy)"/>
      <circle cx="120" cy="263" r="12" fill="var(--navy)"/>
      <rect x="158" y="252" width="22" height="22" fill="var(--teal)"/>
      <polygon points="219,253 231,273 207,273" fill="var(--orange)"/>

      <rect x="59" y="293" width="22" height="22" fill="var(--teal)"/>
      <circle cx="120" cy="304" r="12" fill="var(--navy)"/>
      <polygon points="169,293 181,313 157,313" fill="var(--orange)"/>
      <circle cx="219" cy="304" r="12" fill="var(--navy)"/>

      <circle cx="70" cy="348" r="12" fill="var(--navy)"/>
      <polygon points="120,339 132,359 108,359" fill="var(--orange)"/>
      <circle cx="169" cy="348" r="12" fill="var(--navy)"/>
      <rect x="208" y="337" width="22" height="22" fill="var(--teal)"/>
    </g>

    <g class="sort-dots" fill="var(--dot)">
      <circle cx="245" cy="292" r="2.5"/><circle cx="261" cy="292" r="2.5"/><circle cx="277" cy="292" r="2.5"/>
      <circle cx="293" cy="244" r="2.5"/><circle cx="293" cy="260" r="2.5"/><circle cx="293" cy="276" r="2.5"/>
      <circle cx="293" cy="292" r="2.5"/><circle cx="293" cy="308" r="2.5"/><circle cx="293" cy="324" r="2.5"/><circle cx="293" cy="340" r="2.5"/>
      <circle cx="309" cy="244" r="2.5"/><circle cx="325" cy="244" r="2.5"/><circle cx="341" cy="244" r="2.5"/>
      <circle cx="309" cy="292" r="2.5"/><circle cx="325" cy="292" r="2.5"/><circle cx="341" cy="292" r="2.5"/>
      <circle cx="309" cy="340" r="2.5"/><circle cx="325" cy="340" r="2.5"/><circle cx="341" cy="340" r="2.5"/>
    </g>

    <g class="sorted-groups">
      <circle cx="363" cy="226" r="5.5" fill="var(--navy)"/><circle cx="377" cy="226" r="5.5" fill="var(--navy)"/>
      <circle cx="363" cy="241" r="5.5" fill="var(--navy)"/><circle cx="377" cy="241" r="5.5" fill="var(--navy)"/>
      <polygon points="370,283 375,292 365,292" fill="var(--orange)"/>
      <polygon points="363,295 368,305 358,305" fill="var(--orange)"/>
      <polygon points="365,295 375,295 370,304" fill="var(--orange)"/>
      <polygon points="377,295 382,305 372,305" fill="var(--orange)"/>
      <rect x="356" y="338" width="12" height="12" fill="var(--teal)"/><rect x="370" y="338" width="12" height="12" fill="var(--teal)"/>
      <rect x="356" y="352" width="12" height="12" fill="var(--teal)"/><rect x="370" y="352" width="12" height="12" fill="var(--teal)"/>
    </g>

    <g class="feature-sheet">
      <rect x="482" y="231" width="22" height="22" fill="var(--teal)"/>
      <g fill="var(--dot)">
        <circle cx="523" cy="237" r="2.5"/><circle cx="539" cy="237" r="2.5"/><circle cx="555" cy="237" r="2.5"/><circle cx="571" cy="237" r="2.5"/>
      </g>
      <rect x="609" y="228" width="117" height="117" rx="3" fill="none" stroke="var(--teal)" stroke-width="7"/>
      <g stroke="var(--teal)" stroke-width="6" stroke-linecap="round">
        <line x1="628" y1="245" x2="707" y2="245"/>
        <line x1="628" y1="272" x2="707" y2="272"/>
        <line x1="628" y1="298" x2="707" y2="298"/>
        <line x1="628" y1="324" x2="707" y2="324"/>
      </g>
    </g>

    <g class="doc-tree" fill="none" stroke="var(--grey)" stroke-width="3">
      <polyline points="914,220 914,252 956,252"/>
      <polyline points="976,272 976,350 1016,350"/>
      <line x1="976" y1="303" x2="1016" y2="303"/>
      <rect x="895" y="183" width="38" height="37" fill="#fff"/>
      <rect x="957" y="236" width="37" height="36" fill="#fff"/>
      <rect x="1017" y="286" width="37" height="36" fill="#fff"/>
      <rect x="1017" y="336" width="37" height="37" fill="#fff"/>
      <g stroke-width="2.5">
        <line x1="903" y1="193" x2="925" y2="193"/><line x1="903" y1="201" x2="925" y2="201"/><line x1="903" y1="209" x2="925" y2="209"/>
        <line x1="965" y1="246" x2="986" y2="246"/><line x1="965" y1="254" x2="986" y2="254"/><line x1="965" y1="262" x2="986" y2="262"/>
        <line x1="1025" y1="296" x2="1046" y2="296"/><line x1="1025" y1="304" x2="1046" y2="304"/><line x1="1025" y1="312" x2="1046" y2="312"/>
        <line x1="1025" y1="346" x2="1046" y2="346"/><line x1="1025" y1="354" x2="1046" y2="354"/><line x1="1025" y1="362" x2="1046" y2="362"/>
      </g>
    </g>
  </svg>
</div>
</body>
</html>
```